creative pack design with extended budget for Velmoraq coffee product

- we need a packing design for a new product of coffee for our company Tesmo Kirul located in Uganda.
- specialty Arabica coffee grown at slopes of Mountain Elgon with rich volcanic soils located in Eastern region of Uganda.
-  we have a logo already made and has registered in Uganda. our logo colors are mixture between a lot of brown color and yellow. vacuum  plastic bags.
- there is no restrictions towards your imagination .
-  all details available
- we will launch our product through phases ;
- phase 1 is  a ground coffee : ( Turkish coffee )  2 degrees of roasting which are ( medium dark , light ) of 250 grm
b) roasted beans: 2 degrees ( medium, dark) of 250 grm & 1000 grm
- we need also to highlight the eastern spirit of Turkish coffee
- we  need designs, the info and color only will be changed depending on previous classifications

Target Market(s)
Arab countries, Turkey , Uganda, Europe
Colors
Designer to choose colors to be used in the design.
Requirements
Nice to have
- about nature , Elgon mountain , farmers, freshness, distinctive product, soul of east such as decorated cup of Turkish coffee . these just an ideas but there is no restrictions on your imagination

```html
<!DOCTYPE html>
<html lang="en">
<head>
<meta charset="utf-8">
<title>Velmoraq Ground Coffee – Pack Front</title>
<link href="https://fonts.googleapis.com/css2?family=Bungee&family=Open+Sans:wght@400;600;700&family=Cinzel:wght@700&display=swap" rel="stylesheet">
<style>
  :root {
    --stage: #f1f0ee;
    --silver-light: #fbfbfb;
    --silver-mid: #e4e4e4;
    --silver-dark: #cfcfcf;
    --brown: #4e2a1e;
    --charcoal: #3c3c3c;
    --leaf: #8cc152;
    --leaf-dark: #4f8a1e;
    --band: #86bf4a;
    --ink: #1f1f1f;
    --hill-grey: #a9a9a9;
    --hill-light: #d2d2d2;
    --copper: #9a5a32;
    --cup-cream: #e9e2d4;
    --saucer-blue: #6f86ad;
  }
  * { box-sizing: border-box; margin: 0; padding: 0; }
  html, body { width: 1200px; height: 815px; overflow: hidden; }
  body { background: var(--stage); position: relative; font-family: "Open Sans", sans-serif; }

  .pack-front {
    position: absolute; left: 414px; top: 36px; width: 372px; height: 742px;
    overflow: hidden;
    background:
      repeating-linear-gradient(135deg, rgba(255,255,255,0.35) 0 1px, rgba(0,0,0,0.02) 1px 3px),
      linear-gradient(120deg, var(--silver-mid) 0%, var(--silver-light) 35%, var(--silver-dark) 60%, var(--silver-light) 85%, var(--silver-mid) 100%);
  }

  .brand-mark {
    position: absolute; left: 0; right: 0; top: 40px;
    display: flex; flex-direction: column; align-items: center; gap: 14px;
  }
  .brand-mark .dot { width: 110px; height: 110px; border-radius: 50%; background: var(--brown); }
  .brand-mark .name {
    font-family: "Cinzel", serif; font-weight: 700; font-size: 40px;
    color: var(--brown); letter-spacing: 1px;
  }

  .elgon-landscape {
    position: absolute; left: 0; right: 0; top: 378px; height: 222px;
    background: linear-gradient(180deg,
      rgba(210,210,210,0) 0%,
      var(--hill-light) 18%,
      var(--hill-grey) 48%,
      var(--hill-light) 80%,
      rgba(225,225,225,0) 100%);
  }

  .product-title {
    position: absolute; left: 0; right: 0; text-align: center;
    font-family: "Bungee", sans-serif; line-height: 1; color: #ffffff;
  }
  .product-title.ground {
    top: 262px; font-size: 57px;
    -webkit-text-stroke: 2px var(--charcoal);
    text-shadow: 3px 3px 0 var(--leaf);
  }
  .product-title.coffee {
    top: 345px; font-size: 62px;
    -webkit-text-stroke: 2px var(--brown);
    text-shadow: 3px 3px 0 rgba(78,42,30,0.45);
  }
  .title-rule {
    position: absolute; left: 62px; right: 62px; top: 336px; height: 2px; background: var(--leaf);
  }
  .style-tag {
    position: absolute; left: 60px; right: 44px; top: 416px;
    display: flex; align-items: center; gap: 4px;
    font-size: 10px; color: var(--charcoal); white-space: nowrap;
  }
  .style-tag::before, .style-tag::after {
    content: ""; flex: 1; border-top: 2px dotted var(--charcoal);
  }
  .style-tag::before { flex: 1.4; }

  .turkish-cup {
    position: absolute; left: 76px; top: 474px; width: 228px; height: 172px;
    border-radius: 14px;
    background: linear-gradient(180deg,
      var(--cup-cream) 0%,
      var(--copper) 45%,
      #7a4428 62%,
      var(--saucer-blue) 82%,
      #9fb0cc 100%);
  }

  .certification {
    position: absolute; left: 0; right: 0; top: 661px;
    display: flex; align-items: center; gap: 6px; padding: 0 6px;
    font-size: 10.5px; font-weight: 600; color: var(--leaf-dark); white-space: nowrap;
  }
  .certification::before, .certification::after {
    content: ""; flex: 1; border-top: 3px dotted var(--leaf);
  }
  .roast-band {
    position: absolute; left: 0; right: 10px; top: 678px; height: 32px;
    background: var(--band);
    display: flex; align-items: center; justify-content: center;
    font-size: 13.5px; font-weight: 700; color: var(--ink);
  }
  .net-weight {
    position: absolute; left: 0; right: 0; top: 718px; text-align: center;
    font-size: 11px; font-weight: 600; color: var(--ink);
  }
</style>
</head>
<body>
  <main class="pack-front">
    <div class="brand-mark">
      <span class="dot"></span>
      <span class="name">Velmoraq</span>
    </div>

    <div class="elgon-landscape" role="img" aria-label="Faded greyscale photo of Mount Elgon slopes with trees"></div>

    <h1 class="product-title ground">GROUND</h1>
    <div class="title-rule"></div>
    <h2 class="product-title coffee">COFFEE</h2>
    <p class="style-tag">Turkish coffee</p>

    <div class="turkish-cup" role="img" aria-label="Photo of a decorated Turkish coffee cup in a copper holder on a painted blue saucer"></div>

    <p class="certification">PRODUCT CERTIFICATION TEXT CAN BE PLACED HERE</p>
    <div class="roast-band">2 DEGREES OF ROASTING ( MEDIUM DARK , LIGHT )</div>
    <p class="net-weight">NET WT. 250 G</p>
  </main>
</body>
</html>
```